Premium Juice and Wine Bottle Label

We require a premium label design for a Burgundy style wine bottle - the design should reflect pure and organic theme, with a reference to New Zealand blueberries. The winning design will look high-end, simple but sophisticated. Our logo is attached, refer :

https://www.orvalecellars.co.nz and https://www.pirovane.co.nz/wines/details/coming-soon-showcase/2018

for inspiration.

Target Market(s)

High-end retail grocery stores, wine shops, bars.

Requirements
Must have
• Label should leave enough space for barcode and nutrients/ingredients etc. Reference to New Zealand, natural-beverage, be very high-end in design. Refer links in project description for inspiration. Refer to attached logo, which must be used - feel free to change colour in order to obtain the best high-class design.
Nice to have
• N/A.
Should not have
• Cartoons or pictures of berries.

```html
<!DOCTYPE html>
<html lang="en">
<head>
<meta charset="utf-8">
<title>Kestrel Lane — Premium Juice Bottle Label</title>
<link href="https://fonts.googleapis.com/css2?family=Cormorant+Garamond:wght@500&display=swap" rel="stylesheet">
<style>
  :root {
    --page: #ffffff;
    --berry-deep: #2a3150;
    --berry-mid: #4a5a8e;
    --berry-light: #7084b8;
    --banner: #2b3487;
    --gold: #a59446;
    --gold-line: #f4f1e6;
    --cream: #f7f4e9;
  }
  * { margin: 0; padding: 0; box-sizing: border-box; }
  html, body {
    width: 1200px;
    height: 1194px;
    overflow: hidden;
    background: var(--page);
  }
  .label {
    position: absolute;
    left: 100px;
    top: 97px;
    width: 1000px;
    height: 1000px;
    overflow: hidden;
  }
  .label__photo {
    position: absolute;
    inset: 0;
    background:
      radial-gradient(circle at 30% 35%, var(--berry-light) 0%, transparent 30%),
      radial-gradient(circle at 75% 70%, var(--berry-light) 0%, transparent 28%),
      radial-gradient(circle at 85% 25%, var(--berry-mid) 0%, transparent 25%),
      radial-gradient(circle at 20% 85%, var(--berry-mid) 0%, transparent 30%),
      linear-gradient(160deg, var(--berry-mid), var(--berry-deep));
  }
  .label__band {
    position: absolute;
    left: 0;
    width: 100%;
    top: 116px;
    height: 47px;
    background: var(--gold);
  }
  .label__band-line {
    position: absolute;
    left: 0;
    width: 100%;
    top: 12px;
    height: 4px;
    background: var(--gold-line);
  }
  .label__banner {
    position: absolute;
    left: 0;
    top: 0;
    width: 1000px;
    height: 1000px;
  }
  .label__brand {
    position: absolute;
    left: 251px;
    width: 458px;
    top: 250px;
    text-align: center;
    font-family: "Cormorant Garamond", serif;
    font-weight: 500;
    font-size: 132px;
    line-height: 0.95;
    color: var(--cream);
  }
  .label__origin {
    position: absolute;
    left: 0;
    width: 960px;
    top: 692px;
    text-align: center;
    font-family: "Cormorant Garamond", serif;
    font-weight: 500;
    font-size: 46px;
    letter-spacing: 1px;
    color: var(--cream);
  }
</style>
</head>
<body>
  <section class="label">
    <div class="label__photo" role="img" aria-label="Close-up photograph of fresh blueberries with water droplets"></div>
    <div class="label__band"><div class="label__band-line"></div></div>
    <svg class="label__banner" viewBox="0 0 1000 1000" aria-hidden="true">
      <polygon points="251,116 709,116 709,604 480,677 251,604" fill="var(--banner)"/>
    </svg>
    <h1 class="label__brand">Kestrel<br>Lane</h1>
    <p class="label__origin">NEW ZEALAND</p>
  </section>
</body>
</html>
```